Zielgruppe
Ich berate im Bereich der Telemedizin. Zielgruppe sind Ärzte, Krankenkassen, Politiker.
Aufgabenstellung
Auf der Visitenkarte sollen Adresse, e-mail, Handynummer vorhanden sein.
Briefpapier bitte im Pages-Format.

```html
<!DOCTYPE html>
<html lang="de">
<head>
<meta charset="utf-8">
<title>novacura Telemedizin – Briefpapier</title>
<link rel="stylesheet" href="https://fonts.googleapis.com/css2?family=Open+Sans:wght@400;600;700&display=swap">
<style>
  :root {
    --ink: #4a4a4a;
    --ink-soft: #6b6b6b;
    --brand-green: #8dc63f;
    --accent-tan: #d9b98a;
    --band: #5a5a5a;
    --paper: #ffffff;
  }
  * { margin: 0; padding: 0; box-sizing: border-box; }
  html, body { width: 847px; height: 1200px; overflow: hidden; background: var(--paper); }
  body { font-family: "Open Sans", Arial, sans-serif; color: var(--ink); }

  .letterhead { position: relative; width: 847px; height: 1200px; background: var(--paper); border: 1px solid #d4d4d4; }
  .top-band, .bottom-band { position: absolute; left: 0; width: 100%; background: var(--band); }
  .top-band { top: 0; height: 14px; }
  .bottom-band { bottom: 0; height: 10px; }

  .brand { position: absolute; display: flex; align-items: center; gap: 10px; }
  .brand-dot { border-radius: 50%; background: var(--brand-green); flex: none; }
  .brand-name { font-weight: 700; color: var(--brand-green); line-height: 1; }
  .brand--head { top: 68px; left: 552px; }
  .brand--head .brand-dot { width: 44px; height: 44px; }
  .brand--head .brand-name { font-size: 46px; letter-spacing: 0.5px; }
  .brand--foot { bottom: 36px; left: 14px; gap: 6px; }
  .brand--foot .brand-dot { width: 20px; height: 20px; }
  .brand--foot .brand-name { font-size: 18px; }

  .sender-line {
    position: absolute; top: 190px; left: 84px; width: 326px;
    font-size: 9px; padding-bottom: 4px; border-bottom: 1px solid var(--ink);
    white-space: nowrap;
  }

  .contact-column {
    position: absolute; top: 212px; left: 598px;
    border-left: 1px solid var(--accent-tan);
    padding-left: 12px; font-size: 11.5px; line-height: 16px; font-style: normal;
  }
  .contact-column p + p { margin-top: 14px; }
  .contact-column .place-date { margin-top: 22px; }

  .fold-mark { position: absolute; left: 0; width: 16px; height: 1px; background: var(--ink-soft); }
  .fold-mark--upper { top: 420px; }
  .fold-mark--lower { top: 575px; }
  .window-mark { position: absolute; top: 372px; width: 2px; height: 2px; background: var(--ink-soft); }
  .window-mark--left { left: 84px; }
  .window-mark--right { left: 420px; }

  .footer-columns { position: absolute; bottom: 30px; left: 252px; display: flex; font-size: 9.5px; line-height: 13px; }
  .footer-col { width: 190px; white-space: nowrap; }
  .footer-col:nth-child(3) { width: 200px; }
  .footer-label { color: var(--brand-green); }
</style>
</head>
<body>
<main class="letterhead">
  <div class="top-band"></div>

  <div class="brand brand--head">
    <span class="brand-dot"></span>
    <span class="brand-name">novacura</span>
  </div>

  <div class="sender-line">novacura telemedizin &nbsp;|&nbsp; Lindenweg 14 &nbsp;|&nbsp; 45127 Talheim</div>

  <address class="contact-column">
    <p>Lindenweg 14<br>45127 Talheim</p>
    <p>Tel. 0231 47 19 05<br>Mobil 0171 52 63 84 17</p>
    <p>info@novacura-telemedizin.de<br>www.novacura-telemedizin.de</p>
    <p class="place-date">Talheim, den</p>
  </address>

  <span class="fold-mark fold-mark--upper"></span>
  <span class="fold-mark fold-mark--lower"></span>
  <span class="window-mark window-mark--left"></span>
  <span class="window-mark window-mark--right"></span>

  <div class="brand brand--foot">
    <span class="brand-dot"></span>
    <span class="brand-name">novacura</span>
  </div>

  <footer class="footer-columns">
    <div class="footer-col">
      <div class="footer-label">Inhaber:</div>
      <div>Dr. Henrik Vossberg</div>
      <div>Platz für weiteren Titel</div>
    </div>
    <div class="footer-col">
      <div class="footer-label">Finanzamt Talheim</div>
      <div>USt.-IdNr.:</div>
      <div>DE31749260</div>
    </div>
    <div class="footer-col">
      <div class="footer-label">Sparkasse Talheim</div>
      <div>IBAN: DE00 0000 0000 0000 0000 00</div>
      <div>BIC: XXXXXXXXXX</div>
    </div>
  </footer>

  <div class="bottom-band"></div>
</main>
</body>
</html>
```